Investment company needing business card

We are wanting a business card which looks sharp and easy on the eye. We are thinking of having a business card with the logo embossed on it, to really make it stand out. We will only have a small amount of information of the business card, person's name, position, email address and phone number

Danielle Hartig
Executive Assistant
+64 21 574 3162
danielleh@quarvendale.co.nz

Requirements
Must have
• Embossed logo
Should not have
• Not to be busy

```html
<!DOCTYPE html>
<html lang="en">
<head>
<meta charset="utf-8">
<title>Quarvendale Group – Business Card</title>
<link rel="stylesheet" href="https://fonts.googleapis.com/css2?family=Lato:wght@400;700&display=swap">
<style>
  :root {
    --stage: #2b2b2c;
    --card-grey: #646567;
    --band-grey: #5f6062;
    --brand-green: #22b573;
    --paper: #ffffff;
    --ink-light: #ffffff;
  }
  * { margin: 0; padding: 0; box-sizing: border-box; }
  html, body {
    width: 1200px;
    height: 880px;
    overflow: hidden;
    background: var(--stage);
    font-family: "Lato", sans-serif;
  }
  .canvas {
    position: relative;
    width: 1200px;
    height: 880px;
  }
  .card {
    position: absolute;
    width: 560px;
    height: 320px;
    border-radius: 18px;
    overflow: hidden;
  }
  /* Back of card */
  .card-back {
    left: 90px;
    top: 90px;
    background: var(--card-grey);
    display: flex;
    align-items: center;
    justify-content: center;
  }
  .brand {
    display: flex;
    align-items: center;
    gap: 14px;
  }
  .brand-square {
    width: 34px;
    height: 34px;
    background: var(--brand-green);
  }
  .brand-name {
    font-family: "Lato", sans-serif;
    font-weight: 700;
    font-size: 30px;
    letter-spacing: 3px;
    color: var(--brand-green);
    text-transform: uppercase;
  }
  /* Front of card */
  .card-front {
    left: 550px;
    top: 470px;
    background: var(--paper);
  }
  .card-front .bands {
    position: absolute;
    inset: 0;
  }
  .card-front .band-grey { fill: var(--band-grey); }
  .card-front .band-green { fill: var(--brand-green); }
  .card-front .brand {
    position: absolute;
    left: 42px;
    top: 70px;
  }
  .card-front .brand-name { font-size: 26px; }
  .card-front .brand-square { width: 30px; height: 30px; }
  .person {
    position: absolute;
    left: 42px;
    top: 207px;
    color: var(--ink-light);
    line-height: 1.05;
  }
  .person-name {
    font-weight: 700;
    font-size: 17px;
  }
  .person-role {
    font-weight: 400;
    font-size: 14px;
  }
  .contact {
    position: absolute;
    left: 42px;
    top: 262px;
    list-style: none;
    color: var(--ink-light);
    font-size: 14px;
    line-height: 21px;
  }
  .contact li {
    display: flex;
    align-items: center;
    gap: 8px;
  }
  .contact svg {
    width: 12px;
    height: 12px;
    flex: none;
  }
</style>
</head>
<body>
<main class="canvas">

  <section class="card card-back" aria-label="Business card back">
    <div class="brand">
      <span class="brand-square"></span>
      <span class="brand-name">Quarvendale Group</span>
    </div>
  </section>

  <section class="card card-front" aria-label="Business card front">
    <svg class="bands" viewBox="0 0 560 320" width="560" height="320" aria-hidden="true">
      <path class="band-grey" d="M0 198 H240 Q256 198 258 186 Q261 165 280 165 H560 V320 H0 Z"/>
      <path class="band-green" d="M0 250 H236 Q256 250 258 236 L261 196 Q263 180 282 180 H560 V320 H0 Z"/>
    </svg>

    <div class="brand">
      <span class="brand-square"></span>
      <span class="brand-name">Quarvendale Group</span>
    </div>

    <div class="person">
      <p class="person-name">Danielle Hartig</p>
      <p class="person-role">Executive Assistant</p>
    </div>

    <ul class="contact">
      <li>
        <svg viewBox="0 0 12 12" aria-hidden="true"><rect x="2.5" y="0.8" width="7" height="10.4" rx="1.2" fill="none" stroke="#fff" stroke-width="1.2"/><line x1="5" y1="9.3" x2="7" y2="9.3" stroke="#fff" stroke-width="1"/></svg>
        <span>+64 21 574 3162</span>
      </li>
      <li>
        <svg viewBox="0 0 12 12" aria-hidden="true"><rect x="0.6" y="2.2" width="10.8" height="7.6" fill="#fff"/><path d="M0.6 2.2 L6 6.6 L11.4 2.2" fill="none" stroke="#22b573" stroke-width="1"/></svg>
        <span>danielleh@quarvendale.co.nz</span>
      </li>
    </ul>
  </section>

</main>
</body>
</html>
```